A Referral Pad for a Specialist Surgeon to give to referring GPs

A referral pad allows general practitioners to easily refer patients to me by quickly filling in a form on a small pad that I provide them.

A two sided referral pad themed appropriately. Theming and designing the pad should be based on the general design/logo/imagery/colours etc. from my website www.marcusbelwether.com.au. I have a logo uploaded that should be used somewhere. I have also upload a headshot of myself which might or might not be used. Other choice of imagery and design features is up to the designer.

In terms of size of the pad I’m not quite sure what is best and will leave it up to the designers.

MORE DETAILED INFORMATION IS PROVIDED IN THE UPLOADED WORD FILE

Target Market(s)

General Practitioners referring to me

Industry/Entity Type

Healthcare

Contact Information for Business Card

A business card themed as per the referral pad design as as per general look and imagery found on www.marcusbelwether.com.au

Requirements
Must have
• Referral pad details found in uploaded Word document
Nice to have
Should not have

```html
<!DOCTYPE html>
<html lang="en">
<head>
<meta charset="utf-8">
<title>Marcus Belwether – Patient Referral Pad</title>
<link href="https://fonts.googleapis.com/css2?family=Arimo:wght@400;700&family=Open+Sans:wght@400;700&display=swap" rel="stylesheet">
<style>
  :root {
    --teal: #67aca5;
    --teal-text: #3f9d94;
    --ink: #1a1a1a;
    --paper: #ffffff;
    --backdrop: #f4f5f5;
  }
  * { box-sizing: border-box; margin: 0; padding: 0; }
  html, body { width: 1200px; height: 1000px; overflow: hidden; background: var(--backdrop); }
  .canvas { position: relative; width: 1200px; height: 1000px; }
  .sheet {
    position: absolute; left: 314px; top: 97px; width: 571px; height: 808px;
    background: var(--paper); box-shadow: 0 3px 10px rgba(0,0,0,.25);
    font-family: "Arimo", Arial, sans-serif; color: var(--ink);
  }
  .abs { position: absolute; }
  .brand { left: 36px; top: 20px; display: flex; align-items: center; gap: 10px; }
  .brand-dot { width: 26px; height: 26px; border-radius: 50%; background: var(--teal); }
  .brand-name { font-size: 21px; color: var(--teal-text); letter-spacing: .5px; font-weight: 400; }
  .locations { right: 35px; top: 9px; text-align: right; font-family: "Open Sans", Arial, sans-serif; font-size: 10.5px; line-height: 16.2px; color: var(--teal-text); }
  .locations strong { font-weight: 700; }
  .rule { left: 0; width: 100%; height: 2px; background: var(--teal); }
  .contact { left: 0; width: 100%; text-align: center; font-size: 12px; letter-spacing: 1px; word-spacing: 3px; }
  .contact .sep { margin: 0 12px; }
  .band { left: 0; width: 100%; background: var(--teal); color: #fff; text-align: center; font-weight: 700; }
  .band-title { top: 123px; height: 29px; line-height: 29px; font-size: 19px; letter-spacing: 1.6px; }
  .band-note { top: 420px; height: 20px; line-height: 20px; font-size: 12px; letter-spacing: 1.2px; }
  .field { font-size: 13.5px; letter-spacing: 1px; white-space: nowrap; }
  .line { height: 1px; background: var(--ink); }
  .group-title { font-family: "Open Sans", Arial, sans-serif; font-weight: 700; font-size: 10.5px; letter-spacing: .75px; }
  .group-title.large { font-size: 12px; }
  .option { font-family: "Open Sans", Arial, sans-serif; font-size: 10px; display: flex; align-items: center; gap: 7px; white-space: nowrap; }
  .box { display: inline-block; width: 8px; height: 8px; border: 1.3px solid var(--ink); }
</style>
</head>
<body>
<div class="canvas">
  <section class="sheet">
    <header>
      <div class="abs brand"><span class="brand-dot"></span><span class="brand-name">Marcus Belwether</span></div>
      <div class="abs locations">
        <strong>Melbourne</strong><br>Southbank, Carlton, Hawthorn East<br><strong>Regional</strong><br>Ballarat, Geelong, Warragul
      </div>
      <div class="abs rule" style="top:80px"></div>
      <div class="abs contact" style="top:96px">P: (03) 9000 4182<span class="sep">•</span>F: (03) 9000 4183<span class="sep">•</span>info@belwethersurgery.com.au</div>
      <div class="abs band band-title">PATIENT REFERRAL</div>
    </header>

    <div class="form">
      <span class="abs field" style="left:33px;top:184px">Appointment Date:</span>
      <div class="abs line" style="left:169px;width:167px;top:199px"></div>
      <span class="abs field" style="left:342px;top:184px">Time:</span>
      <div class="abs line" style="left:380px;width:158px;top:199px"></div>

      <span class="abs field" style="left:33px;top:217px">Patient name:</span>
      <div class="abs line" style="left:131px;width:407px;top:232px"></div>
      <span class="abs field" style="left:33px;top:237px">DOB:</span>
      <div class="abs line" style="left:71px;width:278px;top:262px"></div>
      <span class="abs field" style="left:358px;top:247px">Gender: MALE / FEMALE</span>

      <span class="abs field" style="left:33px;top:277px">Phone:</span>
      <div class="abs line" style="left:81px;width:217px;top:292px"></div>
      <span class="abs field" style="left:302px;top:277px">Email:</span>
      <div class="abs line" style="left:345px;width:193px;top:292px"></div>

      <span class="abs field" style="left:33px;top:311px">Referring Dr.:</span>
      <div class="abs line" style="left:130px;width:219px;top:326px"></div>
      <span class="abs field" style="left:353px;top:311px">Phone:</span>
      <div class="abs line" style="left:402px;width:136px;top:326px"></div>

      <span class="abs field" style="left:33px;top:344px">Patient's Medical History:</span>
      <div class="abs line" style="left:217px;width:321px;top:360px"></div>
      <div class="abs line" style="left:33px;width:505px;top:392px"></div>
    </div>

    <div class="abs band band-note">PLEASE BRING THIS FORM TO YOUR APPOINTMENT.</div>

    <div class="checklist">
      <span class="abs group-title" style="left:33px;top:456px">BARIATRIC SURGERY:</span>
      <span class="abs option" style="left:33px;top:486px"><span class="box"></span>Patient weight</span>
      <span class="abs option" style="left:176px;top:486px"><span class="box"></span>Patient BMI</span>
      <span class="abs option" style="left:311px;top:486px"><span class="box"></span>Diabetic</span>

      <span class="abs group-title" style="left:33px;top:518px">ABDOMINOPLASTY OR ARM REDUCTION AFTER WEIGHT LOSS</span>
      <span class="abs box" style="left:449px;top:521px"></span>
      <span class="abs group-title" style="left:33px;top:542px">ANTIREFLUX/HIATUS HERNIA SURGERY</span>
      <span class="abs box" style="left:449px;top:549px"></span>
      <span class="abs group-title" style="left:33px;top:571px">GALLBLADDER</span>
      <span class="abs box" style="left:449px;top:576px"></span>
      <span class="abs group-title" style="left:33px;top:600px">HERNIA</span>
      <span class="abs box" style="left:449px;top:604px"></span>
      <span class="abs group-title" style="left:33px;top:628px">ENDOSCOPY</span>
      <span class="abs box" style="left:449px;top:632px"></span>

      <span class="abs group-title large" style="left:33px;top:668px">OTHER GENERAL SURGERY:</span>
      <span class="abs option" style="left:33px;top:698px"><span class="box"></span>Skin</span>
      <span class="abs option" style="left:164px;top:698px"><span class="box"></span>Lumps &amp; bumps</span>
      <span class="abs option" style="left:305px;top:698px"><span class="box"></span>Peri-anal/haemorrhoids</span>
      <span class="abs option" style="left:33px;top:731px"><span class="box"></span>Varicose veins</span>
      <span class="abs option" style="left:164px;top:731px"><span class="box"></span>Carpal tunnel</span>
    </div>

    <footer>
      <div class="abs rule" style="top:764px"></div>
      <div class="abs contact" style="top:776px">P: (03) 9000 4182<span class="sep">•</span>F: (03) 9000 4183<span class="sep">•</span>info@belwethersurgery.com.au</div>
    </footer>
  </section>
</div>
</body>
</html>
```